Web Design Project

We need a design for the actual web.
http://mirela.vunto.example/
It will be a cakes and cupcakes online shop.

It is a one page site, with five anchors.

Inicio (Home)
Here it will show a brief explanation about our shop, just explaining we sell really nice cakes and cupcakes. Also we want to show a slide gallery, like the one it is working, but with not nice choosen pictures.

Productos/Tortas
This two anchors will be just one at the end, but I wanted to show the two options for accessing the different products, tabs or buttons. You can click on the firsts images on that links for see the "pop up image" with a better explanation of every product.

Contacto
Here it will show a little form, that will only appear in smartphones and maybe tablets, this form needs to be similar and much more simple than the principal form (the next anchor), so just focus on it once the next one its done.

Form
This will be the way the users will send the orders, its a complex form, focused on the UX. We dont want the user to type too much and we want it to surprise the user and fell really comfortable.

Industry/Entity Type

Tv

Requirements
Must have

• -Must have side menu, but you can redesign it completelly, but with the same structure
-Its important to focus all the content in the top and middle, we arent sure about users screens and it we set info at the footer, maybe its not gonna show (no scroll vertical).
-You can change all the colours of the site, we are open to new visions, you can surprise us.

```html
<!DOCTYPE html>
<html lang="es">
<head>
<meta charset="utf-8">
<title>Lina Bakes — Homemade Bakery</title>
<link rel="stylesheet" href="https://fonts.googleapis.com/css2?family=Playball&family=Pacifico&family=Niconne&family=Gochi+Hand&family=Delius&family=Ubuntu:wght@400&display=swap">
<style>
  :root {
    --header-bg: #bfe6f8;
    --header-line: #9fd2ea;
    --page-bg: #f6f0c8;
    --panel-bg: #cdeefc;
    --menu-active: #a7def8;
    --menu-line: #9cc8da;
    --ink: #4a4a4a;
    --brand-ink: #ffffff;
    --script-ink: #2f6f80;
    --title-ink: #3f6f7c;
    --icon-bg: #b9dbea;
    --icon-ring: #8fb8ca;
    --dot: #6f7a80;
    --slide-dark: #6a3a10;
    --slide-warm: #e9c55a;
    --slide-red: #c93a2a;
  }
  * { box-sizing: border-box; margin: 0; padding: 0; }
  html, body { width: 1200px; height: 802px; overflow: hidden; }
  body {
    position: relative;
    background: var(--page-bg);
    font-family: "Ubuntu", sans-serif;
    color: var(--ink);
  }
  .site-header {
    position: absolute; left: 0; top: 0; width: 1200px; height: 78px;
    background: var(--header-bg);
    border-bottom: 3px solid var(--header-line);
  }
  .brand {
    position: absolute; left: 30px; top: 8px;
    display: flex; align-items: center; gap: 18px;
  }
  .brand-mark {
    width: 50px; height: 50px; border-radius: 50%;
    background: var(--icon-bg); border: 2px solid var(--icon-ring);
  }
  .brand-name {
    font-family: "Playball", cursive;
    font-size: 50px; line-height: 60px; color: var(--brand-ink);
  }
  .tagline {
    position: absolute; left: 470px; top: 10px;
    font-family: "Pacifico", cursive; font-size: 30px; line-height: 44px;
    color: var(--script-ink);
  }
  .social { position: absolute; right: 12px; top: 14px; display: flex; gap: 14px; list-style: none; }
  .social li {
    width: 46px; height: 46px; border-radius: 50%;
    background: var(--icon-bg); border: 2px solid var(--icon-ring);
    display: flex; align-items: center; justify-content: center;
  }
  .panel {
    position: absolute; left: 65px; top: 108px; width: 1073px; height: 596px;
    background: var(--panel-bg);
    box-shadow: 0 2px 6px rgba(0,0,0,0.18);
  }
  .side-menu { position: absolute; left: 0; top: 0; width: 235px; height: 596px; list-style: none; }
  .side-menu li {
    display: flex; align-items: center; justify-content: center;
    font-family: "Gochi Hand", cursive; font-size: 28px; color: var(--ink);
    border-bottom: 1px solid var(--menu-line);
  }
  .side-menu li.is-active {
    background: var(--menu-active); font-family: "Ubuntu", sans-serif; font-size: 30px;
    box-shadow: 2px 3px 4px rgba(0,0,0,0.25); border-bottom: none; margin-right: -3px;
  }
  .side-menu li:last-child { border-bottom: none; }
  .page-title {
    position: absolute; left: 258px; top: 18px; width: 792px; text-align: center;
    font-family: "Niconne", cursive; font-size: 40px; font-weight: 400; color: var(--title-ink);
    text-shadow: 0 2px 3px rgba(0,0,0,0.25);
  }
  .slider { position: absolute; left: 258px; top: 91px; width: 792px; height: 427px; }
  .slide-photo {
    position: absolute; inset: 0;
    background: radial-gradient(ellipse at 50% 55%, var(--slide-warm) 0%, #d9a640 40%, var(--slide-red) 70%, var(--slide-dark) 100%);
  }
  .slide-caption {
    position: absolute; right: 60px; top: 6px; text-align: right;
    font-family: "Delius", cursive; font-size: 40px; line-height: 46px; color: #fff;
  }
  .slide-nav {
    position: absolute; top: 0; width: 48px; height: 427px;
    background: rgba(40,30,20,0.55);
    display: flex; align-items: center; justify-content: center;
  }
  .slide-nav.prev { left: 0; }
  .slide-nav.next { right: 0; }
  .slide-dots { position: absolute; left: 322px; top: 534px; display: flex; gap: 19px; list-style: none; }
  .slide-dots li { width: 14px; height: 14px; border-radius: 50%; background: var(--dot); }
  .slide-dots li.is-current { background: transparent; border: 3px solid var(--dot); width: 18px; height: 18px; margin: -2px; }
  .site-footer {
    position: absolute; left: 0; top: 726px; width: 1200px; text-align: center;
    font-size: 15px; line-height: 19px; color: #333;
  }
</style>
</head>
<body>
  <header class="site-header">
    <div class="brand">
      <span class="brand-mark"></span>
      <span class="brand-name">Lina Bakes</span>
    </div>
    <div class="tagline">Homemade Bakery</div>
    <ul class="social">
      <li><svg width="26" height="20" viewBox="0 0 26 20"><rect x="1" y="1" width="24" height="18" fill="#fff" stroke="#8a9aa2" stroke-width="1.5"/><path d="M1 1 L13 11 L25 1" fill="none" stroke="#8a9aa2" stroke-width="1.5"/></svg></li>
      <li></li>
      <li></li>
      <li></li>
    </ul>
  </header>

  <main class="panel">
    <ul class="side-menu">
      <li class="is-active" style="height:111px">INICIO</li>
      <li style="height:122px">PRODUCTOS</li>
      <li style="height:113px">TORTAS</li>
      <li style="height:125px">CONTACTO</li>
      <li style="height:125px">FORM</li>
    </ul>

    <h1 class="page-title">Los mejores Cupcakes y Pasteles de Santiago</h1>

    <section class="slider">
      <div class="slide-photo" role="img" aria-label="Fotografía de una torta de chocolate blanco con frambuesas, cortada en un plato floral"></div>
      <div class="slide-caption">torta chocolate<br>blanco frambuesa</div>
      <div class="slide-nav prev"><svg width="24" height="44" viewBox="0 0 24 44"><path d="M22 2 L3 22 L22 42" fill="none" stroke="#fff" stroke-width="3"/></svg></div>
      <div class="slide-nav next">
        <svg width="24" height="44" viewBox="0 0 24 44"><path d="M2 2 L21 22 L2 42" fill="none" stroke="#fff" stroke-width="3"/></svg>
        <svg style="position:absolute;bottom:10px;left:16px" width="16" height="16" viewBox="0 0 16 16"><circle cx="8" cy="8" r="7" fill="none" stroke="#ccc" stroke-width="1.2"/><path d="M6 4.5 L11 8 L6 11.5Z" fill="#ccc"/></svg>
      </div>
    </section>

    <ul class="slide-dots">
      <li></li><li class="is-current"></li><li></li><li></li><li></li><li></li>
    </ul>
  </main>

  <footer class="site-footer">
    © 2012 lina bakes<br>
    email- info@linabakes.example | hotline 000-000 00000
  </footer>
</body>
</html>
```